Bao Lotus Menu Design Project

This project is pretty straight forward. You will be given 3 files which include the following:
1. Our proposed menu
2. Our Company logo
3. A sample menu on what we are looking for design wise

Your job is to create a visually pleasing menu that is simple, clean and fresh. Please refer to our home website for additional information. (www.baolotus-example.com) Must be in eps or equivalent format.

Target Market(s)

20s to 40s

Industry/Entity Type

It Company

Requirements
Must have
• Company log
Must be in EPS format

```html
<!DOCTYPE html>
<html lang="en">
<head>
<meta charset="utf-8">
<title>Bao Lotus Menu – Vegetables, Gluten Free, Mushu &amp; Rice</title>
<link href="https://fonts.googleapis.com/css2?family=Josefin+Sans:ital,wght@0,400;0,600;0,700;1,400&display=swap" rel="stylesheet">
<style>
  :root {
    --ink: #ffffff;
    --accent: #c8202a;
    --gold: #c9a24a;
    --night: #141214;
    --ember: #8a1e17;
  }
  html, body { margin: 0; padding: 0; overflow: hidden; }
  body { width: 1200px; height: 1000px; background: var(--night); font-family: "Josefin Sans", sans-serif; color: var(--ink); }
  .menu-spread { position: relative; width: 1200px; height: 1000px; overflow: hidden; }
  .backdrop {
    position: absolute; inset: 0;
    background:
      radial-gradient(ellipse 700px 260px at 600px -40px, rgba(201,162,74,.85), rgba(201,162,74,0) 70%),
      linear-gradient(90deg, rgba(201,162,74,.7) 0, rgba(201,162,74,0) 70px, rgba(201,162,74,0) 1130px, rgba(201,162,74,.7) 1200px),
      linear-gradient(180deg, #2a2218 0, #171416 35%, #1a1314 60%, #4a1a14 85%, #a02a1c 100%);
  }
  .divider { position: absolute; left: 597px; top: 42px; width: 3px; height: 908px; background: var(--accent); }
  .column { position: absolute; top: 38px; }
  .column--left { left: 58px; width: 480px; }
  .column--right { left: 657px; width: 480px; }
  .section-title { margin: 0; text-align: center; color: var(--accent); font-weight: 400; font-size: 25px; letter-spacing: .5px; text-transform: uppercase; }
  .section-note { margin: 18px 0 48px; text-align: center; font-weight: 700; font-size: 17.5px; line-height: 22px; }
  .dish { margin: 0; font-size: 17px; line-height: 22.5px; }
  .dish-head { display: flex; justify-content: space-between; font-weight: 700; }
  .dish-desc { margin: 0; font-style: italic; text-align: right; }
  .placeholder .dish-head { font-weight: 700; }
  .placeholder .dish-head.light { font-weight: 400; font-style: italic; }
  .placeholder .fill { white-space: nowrap; overflow: hidden; font-style: italic; letter-spacing: .2px; }
  .placeholder .fill-end { text-align: right; font-style: italic; }
  .gluten-list { margin-top: 20px; }
  .gluten-list .dish { margin-bottom: 6px; }
  .mushu-title { margin-top: 8px; }
  .mushu-list { margin-top: 18px; padding-left: 8px; }
  .price-pair { display: flex; gap: 16px; }
  .brand-mark { position: absolute; bottom: 30px; font-weight: 700; font-size: 15px; color: var(--accent); line-height: 1; }
  .brand-mark--left { left: 16px; }
  .brand-mark--right { right: 16px; }
</style>
</head>
<body>
<main class="menu-spread">
  <div class="backdrop" role="img" aria-label="Dark background with a gold and red layered wave pattern"></div>
  <div class="divider"></div>

  <section class="column column--left">
    <h2 class="section-title">Vegetables</h2>
    <p class="section-note">Enjoy a Half Chinese Chicken Salad or Plain Fried<br>Rice with any entrée for $5.50<br>Can add Tofu for $1.50</p>

    <article class="dish"><div class="dish-head"><span>Fragrant Vegetables</span><span>8.95</span></div>
      <p class="dish-desc">Mixed vegetables with white wine, curry, garlic, black bean, kungpao, or vegetarian sauce.</p></article>
    <article class="dish"><div class="dish-head"><span>Vegetable Lettuce Wraps</span><span>9.95</span></div>
      <p class="dish-desc">Black mushrooms, bell peppers, water chestnuts, smoked tofu, pine nuts, and white crunchies. Served with four lettuce cups.</p></article>
    <article class="dish"><div class="dish-head"><span>Szechuan String Beans</span><span>8.95</span></div>
      <p class="dish-desc">Blue lake green beans and garlic sautéed with pickled szechwan vegetables.</p></article>
    <article class="dish"><div class="dish-head"><span>Tofu With Black Mushrooms</span><span>7.95</span></div>
      <p class="dish-desc">Fried tofu triangles sautéed with scallions, black mushrooms, water chestnuts, and cabbage.</p></article>
    <article class="dish"><div class="dish-head"><span>Bok Choy With Black Mushrooms</span><span>6.95</span></div>
      <p class="dish-desc">Baby bokchoy and black mushrooms sautéed in a brown sauce.</p></article>
    <article class="dish"><div class="dish-head"><span>Spicy Garlic Eggplant</span><span>8.95</span></div>
      <p class="dish-desc">Sautéed chinese eggplant, red onions, and scallions in a spicy garlic sauce.</p></article>
    <article class="dish"><div class="dish-head"><span>Salt And Pepper Tofu</span><span>7.95</span></div>
      <p class="dish-desc">Lightly battered soft tofu cubes with a pepper spice with bell peppers and white crunchies.</p></article>
    <article class="dish"><div class="dish-head"><span>Spinach With Garlic</span><span>6.95</span></div>
      <p class="dish-desc">Sautéed spinach with garlic.</p></article>
  </section>

  <section class="column column--right">
    <h2 class="section-title">Gluten Free</h2>
    <div class="gluten-list">
      <article class="dish placeholder"><div class="dish-head light"><span>XXXXXXX</span><span>zzzz</span></div>
        <div class="fill">yyyyyyyyyyyyyyyyyyyyyyyyyyyyyyyyyyyyyyyyyyyyyyyyyyyyyyyyyyyyyyyyyy</div><div class="fill-end">yyyyyyyyyyyyyyy</div></article>
      <article class="dish placeholder"><div class="dish-head"><span>XXXXXXXX</span><span>zzzz</span></div>
        <div class="fill">yyyyyyyyyyyyyyyyyyyyyyyyyyyyyyyyyyyyyyyyyyyyyyyyyyyyyyyyyyyyyyyyyy</div><div class="fill-end">yyyyyyyyyyyyyyy</div></article>
      <article class="dish placeholder"><div class="dish-head"><span>XXXXXXXX</span><span>zzzz</span></div>
        <div class="fill">yyyyyyyyyyyyyyyyyyyyyyyyyyyyyyyyyyyyyyyyyyyyyyyyyyyyyyyyyyyyyyyyyy</div><div class="fill-end">yyyyyyyyyyyyyyy</div></article>
      <article class="dish placeholder"><div class="dish-head"><span>XXXXXXXX</span><span>zzzz</span></div>
        <div class="fill">yyyyyyyyyyyyyyyyyyyyyyyyyyyyyyyyyyyyyyyyyyyyyyyyyyyyyyyyyyyyyyyyyy</div><div class="fill-end">yyyyyyyyyyyyyyy</div></article>
      <article class="dish placeholder"><div class="dish-head"><span>XXXXXXXX</span><span>zzzz</span></div>
        <div class="fill">yyyyyyyyyyyyyyyyyyyyyyyyyyyyyyyyyyyyyyyyyyyyyyyyyyyyyyyyyyyyyyyyyy</div><div class="fill-end">yyyyyyyyyyyyyyy</div></article>
      <article class="dish placeholder"><div class="dish-head"><span>XXXXXXXX</span><span>zzzz</span></div>
        <div class="fill">Yyyyyyyyyyyyyyyyyyyyyyyyyyyyyyyyyyyyyyyyyyyyyyyyyyyyyyyyyyyyyyyyyy</div><div class="fill-end">yyyyyyyyyyyyyyy</div></article>
    </div>

    <h2 class="section-title mushu-title">Mushu &amp; Rice</h2>
    <div class="mushu-list">
      <article class="dish"><div class="dish-head"><span>Crab And Asparagus Fried Rice</span><span>13.95</span></div>
        <p class="dish-desc">White fried rice with dungeness crab, asparagus, and egg white topped with fried onions. No soy sauce.</p></article>
      <article class="dish"><div class="dish-head"><span>Yang Chow Rice</span><span>9.25</span></div>
        <p class="dish-desc">White fried rice with shrimp, barbeque pork, peas, carrots, and eggs. No soy sauce.</p></article>
      <article class="dish"><div class="dish-head"><span>Mushu</span><span>7.95</span></div>
        <p class="dish-desc">Chicken, pork, or vegetable mushu with sautéed vegetables, mushrooms, and eggs. Wrapped in two thin pancakes. For shrimp, add $1.00.</p></article>
      <article class="dish"><div class="dish-head"><span>Fried Rice</span><span>7.95</span></div>
        <p class="dish-desc">Chicken, pork, or vegetable with eggs, scallions, and fried rice sauce. For beef or shrimp, add $1.00. For soft tofu, add $1.00. For deep-Fried tofu, add $1.50.</p></article>
      <article class="dish"><div class="dish-head"><span>Steamed Rice</span><span class="price-pair" style="margin-right:14px"><span>SM.</span><span>LG.</span></span></div>
        <div class="dish-head" style="font-weight:400"><span style="font-style:italic">Choice of White or Brown.</span><span class="price-pair" style="font-weight:700"><span>1.25</span><span>1.75</span></span></div></article>
    </div>
  </section>

  <div class="brand-mark brand-mark--left">Bao Lotus</div>
  <div class="brand-mark brand-mark--right">Bao Lotus</div>
</main>
</body>
</html>
```